Roofing Company Sales Rep Business Card

Business card for sales rep to canvass and hand out to property owners/managers for free roof inspections and roof replacements.

```html
<!DOCTYPE html>
<html lang="en">
<head>
<meta charset="utf-8">
<title>Ridgeline Roofing – Business Card</title>
<link href="https://fonts.googleapis.com/css2?family=Arimo:wght@400;700&display=swap" rel="stylesheet">
<style>
  :root {
    --stage: #331c1c;
    --brand-red: #e20000;
    --ink: #2b2b2b;
    --paper: #ffffff;
    --rule: #555555;
    --accent-edge: #1ea0e6;
  }
  * { margin: 0; padding: 0; box-sizing: border-box; }
  html, body { width: 1200px; height: 654px; overflow: hidden; }
  body {
    background: var(--stage);
    font-family: "Arimo", Arial, sans-serif;
    position: relative;
  }
  .card {
    position: absolute;
    top: 178px;
    width: 520px;
    height: 297px;
    box-shadow: 0 8px 24px rgba(0,0,0,.45);
  }
  .card--front { left: 50px; background: var(--paper); border-bottom: 2px solid var(--accent-edge); }
  .card--back { left: 630px; background: var(--brand-red); color: var(--paper); }

  .wordmark {
    display: flex;
    align-items: center;
    gap: 10px;
    font-weight: 700;
    text-transform: uppercase;
    letter-spacing: 1px;
    line-height: 1;
  }
  .wordmark__square { width: 14px; height: 14px; flex: none; }

  .card--front .wordmark {
    position: absolute;
    left: 34px;
    top: 70px;
    width: 230px;
    color: var(--brand-red);
    font-size: 26px;
    line-height: 1.15;
  }
  .card--front .wordmark__text { display: block; max-width: 200px; }
  .card--front .wordmark__square { background: var(--brand-red); }

  .identity { position: absolute; left: 290px; top: 52px; width: 200px; }
  .identity__name { font-weight: 700; font-size: 22px; color: var(--ink); letter-spacing: .5px; }
  .identity__title { font-size: 16px; color: var(--ink); margin-top: 2px; }
  .identity__rule { height: 1px; background: var(--rule); margin-top: 10px; }

  .contact-list { position: absolute; left: 290px; top: 138px; list-style: none; width: 220px; }
  .contact-list li { display: flex; gap: 8px; font-size: 10.5px; color: var(--ink); line-height: 1.4; margin-bottom: 6px; }
  .contact-list svg { width: 13px; height: 13px; flex: none; margin-top: 1px; }

  .card--back .wordmark { position: absolute; left: 0; right: 0; top: 112px; justify-content: center; font-size: 32px; color: var(--paper); }
  .card--back .wordmark__square { background: var(--paper); width: 16px; height: 16px; }
  .card--back .site { position: absolute; left: 0; right: 0; top: 170px; text-align: center; font-size: 13px; letter-spacing: .5px; }
</style>
</head>
<body>
  <section class="card card--front" aria-label="Business card front">
    <div class="wordmark"><span class="wordmark__square"></span><span class="wordmark__text">Ridgeline Roofing</span></div>

    <div class="identity">
      <p class="identity__name">DANA K</p>
      <p class="identity__title">CEO</p>
      <div class="identity__rule"></div>
    </div>

    <ul class="contact-list">
      <li>
        <svg viewBox="0 0 16 16" aria-hidden="true"><circle cx="8" cy="8" r="8" fill="#e20000"/><path d="M8 3.5a3 3 0 0 0-3 3c0 2.2 3 5.5 3 5.5s3-3.3 3-5.5a3 3 0 0 0-3-3z" fill="#fff"/><circle cx="8" cy="6.5" r="1.1" fill="#e20000"/></svg>
        <span>412 Harbor View Road | Suite 210<br>Bayside | CA | 90000</span>
      </li>
      <li>
        <svg viewBox="0 0 16 16" aria-hidden="true"><circle cx="8" cy="8" r="8" fill="#e20000"/><rect x="4" y="5" width="8" height="6" fill="#fff"/><path d="M4 5l4 3.5L12 5" stroke="#e20000" stroke-width=".9" fill="none"/></svg>
        <span>danak@ridgelineroof.com</span>
      </li>
      <li>
        <svg viewBox="0 0 16 16" aria-hidden="true"><circle cx="8" cy="8" r="8" fill="#e20000"/><path d="M5.5 4.2l1.4-.2.8 2-1 .8a5.5 5.5 0 0 0 2.5 2.5l.8-1 2 .8-.2 1.4c-3.8.3-6.6-2.5-6.3-6.3z" fill="#fff"/></svg>
        <span>Main: 555.014.2231<br>Direct: 555.014.2238<br>Fax: 555.019.4470</span>
      </li>
      <li>
        <svg viewBox="0 0 16 16" aria-hidden="true"><circle cx="8" cy="8" r="8" fill="#e20000"/><circle cx="8" cy="8" r="4" fill="none" stroke="#fff" stroke-width="1"/><path d="M4 8h8M8 4c-2 2.5-2 5.5 0 8M8 4c2 2.5 2 5.5 0 8" stroke="#fff" stroke-width=".8" fill="none"/></svg>
        <span>www.ridgelineroof.com</span>
      </li>
    </ul>
  </section>

  <section class="card card--back" aria-label="Business card back">
    <div class="wordmark"><span class="wordmark__square"></span>Ridgeline Roofing</div>
    <p class="site">www.ridgelineroof.com</p>
  </section>
</body>
</html>
```